web page look and feel - B2B enterprise application

We have an enterprise application with 10 to 15 core pages and several supporting pages or popups. To start, we want the graphical design of the Users, Roles and Data Source pages and their supporting popups, wizards, etc. to be made beautiful. That is around 10 pages in total. There is a fair amount of redundancy among the pages. I have attached 5 screenshots. We very much want the pages to project a premium feel. That is absolutely essential. The color scheme is blue and sometimes yellow (only if it makes the page look better) plus black, gray and white. If the design of these screens goes well, we would expand the project to continue with other pages. The core of what we are looking for is graphic in nature but we are open to workflow suggestions if you have them. The Roles screen needs some improvements to the layout. I am looking for everything that includes icons, fonts, spacing, etc. I assume getting to the final design will take some back and forth with multiple revisions.

Target Market(s)

Large Enterprises

Number of Pages Required

5+ page

Requirements
Must have
• Premium feel

```html
<!DOCTYPE html>
<html lang="en">
<head>
<meta charset="utf-8">
<title>Roles – Northvale Data</title>
<link href="https://fonts.googleapis.com/css2?family=Roboto:wght@400;500;700&display=swap" rel="stylesheet">
<style>
  :root {
    --sidebar: #434859;
    --brand-bar: #2f3347;
    --topbar: #dfe3e6;
    --accent: #f5c830;
    --ink: #2f3347;
    --text: #3a3f4d;
    --nav-text: #ffffff;
    --rule: #e1e4e8;
    --page: #ffffff;
  }
  * { margin: 0; padding: 0; box-sizing: border-box; }
  html, body { width: 1200px; height: 1200px; overflow: hidden; background: var(--page); font-family: "Roboto", sans-serif; }
  .app { position: relative; width: 1200px; height: 1200px; }
  .brand { position: absolute; left: 0; top: 0; width: 360px; height: 80px; background: var(--brand-bar); display: flex; align-items: center; padding-left: 30px; gap: 12px; }
  .brand-dot { width: 14px; height: 14px; border-radius: 50%; background: var(--accent); }
  .brand-name { color: #fff; font-size: 28px; font-weight: 500; letter-spacing: -0.5px; }
  .topbar { position: absolute; left: 360px; top: 0; width: 840px; height: 80px; background: var(--topbar); }
  .sidebar { position: absolute; left: 0; top: 80px; width: 360px; height: 920px; background: var(--sidebar); }
  .nav-item { position: absolute; color: var(--nav-text); font-size: 18px; line-height: 1; display: flex; align-items: center; }
  .nav-item svg { position: absolute; left: -38px; width: 22px; height: 22px; fill: #fff; }
  .nav-sub { position: absolute; color: var(--nav-text); font-size: 14px; line-height: 1; }
  .nav-sub.is-active { color: var(--accent); }
  .title { position: absolute; left: 458px; top: 114px; font-size: 24px; font-weight: 700; color: var(--ink); }
  .add-btn { position: absolute; left: 538px; top: 117px; width: 66px; height: 22px; border: 1px solid #8a8f9c; border-radius: 11px; font-size: 11px; color: #6b7080; display: flex; align-items: center; justify-content: center; }
  .roles-table { position: absolute; left: 437px; top: 165px; width: 700px; border-collapse: collapse; font-size: 12px; color: var(--text); }
  .roles-table th { background: var(--topbar); font-weight: 500; text-align: left; height: 29px; padding-left: 20px; color: var(--ink); }
  .roles-table td { height: 29px; padding-left: 20px; border: 1px solid var(--rule); }
  .roles-table col.c1 { width: 170px; } .roles-table col.c2 { width: 176px; } .roles-table col.c3 { width: 188px; } .roles-table col.c4 { width: 166px; }
  .perm { display: inline-block; width: 72px; }
</style>
</head>
<body>
<div class="app">
  <header class="brand"><span class="brand-dot"></span><span class="brand-name">Northvale Data</span></header>
  <div class="topbar"></div>

  <nav class="sidebar">
    <div class="nav-item" style="left:68px;top:42px">
      <svg viewBox="0 0 22 22"><circle cx="11" cy="6" r="5"/><path d="M1 20c0-6 4-8 10-8s10 2 10 8z"/></svg>Users</div>
    <div class="nav-sub is-active" style="left:104px;top:87px">Roles</div>
    <div class="nav-sub" style="left:104px;top:120px">Notification Groups</div>
    <div class="nav-item" style="left:68px;top:161px">
      <svg viewBox="0 0 22 22"><path d="M1 1h14v16H1z" fill="none" stroke="#fff" stroke-width="1.5"/><circle cx="17" cy="17" r="3.5" fill="none" stroke="#fff" stroke-width="1.5"/></svg>Data Sources</div>
    <div class="nav-sub" style="left:140px;top:202px">Data Object Relationships</div>
    <div class="nav-item" style="left:68px;top:243px">
      <svg viewBox="0 0 26 22"><ellipse cx="6" cy="8" rx="6" ry="3"/><rect x="0" y="8" width="12" height="6"/><ellipse cx="19" cy="11" rx="6" ry="3"/><rect x="13" y="11" width="12" height="3"/></svg>Data Sets</div>
    <div class="nav-item" style="left:68px;top:286px">
      <svg viewBox="0 0 22 22"><circle cx="6" cy="4" r="3"/><rect x="2" y="9" width="4" height="12"/><rect x="8" y="12" width="4" height="9"/><rect x="14" y="6" width="4" height="15"/></svg>Rule Sets</div>
    <div class="nav-item" style="left:68px;top:329px">
      <svg viewBox="0 0 22 22"><rect x="1" y="2" width="20" height="14" rx="1" fill="none" stroke="#fff" stroke-width="2"/><circle cx="11" cy="9" r="4"/><rect x="6" y="18" width="10" height="2"/></svg>Schedule</div>
    <div class="nav-item" style="left:68px;top:373px">
      <svg viewBox="0 0 22 22"><ellipse cx="5" cy="10" rx="4" ry="2"/><rect x="1" y="10" width="8" height="9"/><ellipse cx="16" cy="10" rx="4" ry="2"/><rect x="12" y="10" width="8" height="9"/><path d="M6 5h10l-2-2M16 5l-2 2" stroke="#fff" fill="none" stroke-width="1.5"/></svg>Metadata import\export</div>
    <div class="nav-sub" style="left:104px;top:418px">Import</div>
    <div class="nav-sub" style="left:104px;top:451px">Export</div>
  </nav>

  <h1 class="title">Roles</h1>
  <div class="add-btn">+ ADD</div>

  <table class="roles-table">
    <colgroup><col class="c1"><col class="c2"><col class="c3"><col class="c4"></colgroup>
    <thead><tr><th>Rule Name</th><th>Data Sources</th><th>Data Sets</th><th>Rule Sets</th></tr></thead>
    <tbody>
      <tr><td>System administrator</td><td><span class="perm">Read</span>Write</td><td>System administrator</td><td>System administrator</td></tr>
      <tr><td>Role 1</td><td>Role 1</td><td>Role 1</td><td>Role 1</td></tr>
      <tr><td>Read Only</td><td>Read Only</td><td>Read Only</td><td>Read Only</td></tr>
      <tr><td>Data Administrator</td><td>Data Administrator</td><td>Data Administrator</td><td>Data Administrator</td></tr>
    </tbody>
  </table>
</div>
</body>
</html>
```